Attractive WP design (Astra) for our textile production and trading business

We need a design for our new website. We would like it to be based on the WP theme Astra.

1) Description of the business
Kelvaro GmbH is a textile company that is specialized in production and trading of high-quality cotton fabrics/products.

We…
• design and develop
• weave (incl. special weaving/embroidery technique)
• shear
• finish the products (Logo printing, packing)

Our products are…
• Swiss Ghutra
• Shemagh (=Yashmagh) (https://www.vontrema.ch/en/competence/clothing-textiles/clothing-for-arab-and-african-markets/#210)
• Desdasha’s (https://www.vontrema.ch/en/competence/clothing-textiles/clothing-for-arab-and-african-markets/#210)
• Emmas and Shawls
Emmas are traditional head coverings worn by Muslim man in Sudan. The cloth of exactly 5 yards in length is winded around the head like a turban. The cloth can be plain white, have a decorative trim or be colored. There are also matching scarfs.
• Brocade/Damask
• Atiku
• Teminor Voile (https://plovadesk.com/products/teminor-3?_pos=2&_sid=98a067e86&_ss=r)
--> Please see attached pictures of the different fabrics and products

2) Target audience and users
• (Foreign) wholesalers interested in trading with Kelvaro

3) Goals of the website
Kelvaro has been a family-run textile business for 17 years with no web presence. The majority of our historical sales have been based on pre-existing relationships or word-of-mouth connections. Now, we seek to diversify our customer base. For this, we want our first website/online presence in order to:

• Enable foreign wholesalers to discover Kelvaro as a supplier of Swiss quality fabric;
• Showcase both our current specific product line as well as our general manufacturing capabilities for new custom products;
• Enable inquiries/orders by interested parties

4) Design wishes
The design should reflect our high quality textiles. The design should be clean, inviting, friendly and professional. Colors can be chosen freely. Pictures should not overload sites but support our goal to attract and inspire future buyers.

If you have any questions, please reach out to us!

• the site will be multilingual (german/english/possibly french)

```html
<!DOCTYPE html>
<html lang="en">
<head>
<meta charset="utf-8">
<title>Kelvaro GmbH – High Quality Cotton Fabrics</title>
<link href="https://fonts.googleapis.com/css2?family=Roboto:wght@300;400;500;700;900&family=Fira+Sans:wght@400;500;600&display=swap" rel="stylesheet">
<style>
:root{
  --ink:#1b1b1b;
  --text:#333;
  --muted:#666;
  --light-bg:#f7f7f7;
  --white:#fff;
  --footer:#242424;
  --footer-text:#e6e6e6;
  --line:#d9d9d9;
  --grey-btn:#5c5c5c;
}
*{box-sizing:border-box;margin:0;padding:0}
html,body{width:1200px;height:3575px;overflow:hidden}
body{position:relative;background:var(--white);font-family:"Fira Sans",sans-serif;color:var(--text)}
.abs{position:absolute}
.center{text-align:center}

/* header */
.site-header{position:absolute;left:0;top:0;width:1200px;height:93px;background:var(--white);z-index:3;box-shadow:0 1px 3px rgba(0,0,0,.06)}
.brand-tab{position:absolute;left:120px;top:0;width:150px;height:128px;background:var(--white);z-index:4;display:flex;flex-direction:column;align-items:center;justify-content:center;gap:6px;clip-path:polygon(0 0,100% 0,100% 80%,85% 100%,15% 100%,0 80%)}
.brand-mark{width:44px;height:44px;border:3px solid var(--ink);border-radius:50%}
.brand-name{font-family:"Roboto",sans-serif;font-weight:700;font-size:28px;color:var(--ink)}
.main-nav a{position:absolute;top:38px;font-family:"Roboto",sans-serif;font-weight:500;font-size:14px;color:var(--ink);text-decoration:none;letter-spacing:.2px}
.main-nav a.active{text-decoration:underline;text-underline-offset:4px}
.lang{position:absolute;left:993px;top:32px;width:63px;height:26px;border:1px solid #bbb;font-family:"Roboto",sans-serif;font-size:13px;font-weight:500;padding:5px 0 0 14px}
.lang svg{position:absolute;right:10px;top:9px}

/* hero */
.hero{position:absolute;left:0;top:93px;width:1200px;height:667px;background:linear-gradient(90deg,#3a3a3a 0%,#d9d3cf 18%,#f1efee 45%,#f4f4f2 70%,#6f8f4f 90%,#3e6a2e 100%)}
.hero-title{position:absolute;left:576px;top:70px;font-family:"Roboto",sans-serif;font-weight:900;font-size:49px;line-height:56px;color:var(--ink)}
.btn-outline{position:absolute;border:2px solid var(--ink);background:transparent;font-family:"Roboto",sans-serif;font-weight:500;font-size:15px;color:var(--ink);display:flex;align-items:center;justify-content:center;letter-spacing:.3px}
.hero .btn-outline{left:577px;top:258px;width:168px;height:42px;border-width:3px;font-size:14px}
.dots{position:absolute;left:576px;top:333px;display:flex;gap:7px;align-items:center}
.dots span{width:15px;height:15px;border:2px solid var(--ink);border-radius:50%}
.dots span.on{width:20px;height:20px}

/* products */
.products{position:absolute;left:0;top:760px;width:1200px;height:737px;background:var(--light-bg)}
.eyebrow{font-family:"Roboto",sans-serif;font-weight:300;font-size:23px;color:#555;width:1200px;position:absolute;left:0}
.section-title{font-family:"Roboto",sans-serif;font-weight:700;font-size:39px;color:var(--ink);width:1200px;position:absolute;left:0;letter-spacing:.5px}
.product-card{position:absolute;top:180px;width:286px}
.product-img{width:286px;height:247px}
.product-card h3{margin-top:26px;font-family:"Roboto",sans-serif;font-weight:600;font-size:17px;color:var(--ink);text-align:center}
.product-card p{margin-top:14px;font-size:14.5px;line-height:23px;text-align:center;color:#444}
.carousel-arrow{position:absolute;top:321px}

/* welcome */
.welcome-img{position:absolute;left:143px;top:1576px;width:517px;height:498px;background:linear-gradient(160deg,#c9b9a2 0%,#e9e6e1 40%,#bfbab4 70%,#2c2c2c 100%)}
.welcome h2{position:absolute;left:746px;top:1597px;font-family:"Roboto",sans-serif;font-weight:700;font-size:49px;line-height:49px;color:#2a2a2a}
.welcome .rule{position:absolute;left:746px;top:1726px;width:96px;height:3px;background:var(--ink)}
.welcome p{position:absolute;left:746px;top:1752px;width:320px;font-size:19.5px;line-height:25.5px;color:#2c2c2c}

/* what we do */
.process{position:absolute;left:0;top:2157px;width:1200px;height:444px;background:linear-gradient(180deg,#f5f4f4,#efeded)}
.bar{position:absolute;height:4px;background:var(--ink)}
.step{position:absolute;width:180px;text-align:center}
.step .icon{width:86px;height:86px;border:2px solid #666;border-radius:50%;margin:0 auto;background:var(--white);display:flex;align-items:center;justify-content:center}
.step h4{margin-top:20px;font-family:"Roboto",sans-serif;font-weight:400;font-size:19px;line-height:25px;color:var(--ink)}
.step p{margin-top:6px;font-family:"Roboto",sans-serif;font-size:13px;line-height:18px;color:#222}

/* enquiry */
.enquiry-title{top:2665px}
.field{position:absolute;border:1px solid var(--line);background:var(--white);box-shadow:0 2px 4px rgba(0,0,0,.08);font-size:14px;color:#777;padding:0 21px;display:flex;align-items:center}
.field.msg{align-items:flex-start;padding-top:17px}
.btn-dark{position:absolute;left:499px;top:2978px;width:201px;height:47px;background:#262626;color:var(--white);font-family:"Roboto",sans-serif;font-weight:700;font-size:17px;display:flex;align-items:center;justify-content:center;letter-spacing:.5px;box-shadow:0 4px 8px rgba(0,0,0,.25)}

/* footer */
.site-footer{position:absolute;left:0;top:3107px;width:1200px;height:468px;background:var(--footer);color:var(--footer-text)}
.footer-brand{position:absolute;left:144px;top:70px;display:flex;align-items:center;gap:12px;font-weight:600;font-size:34px;color:var(--white)}
.footer-brand .mark{width:36px;height:36px;border:3px solid var(--white);border-radius:50%}
.social{position:absolute;left:145px;top:183px;display:flex;gap:11px}
.social span{width:30px;height:30px;border-radius:50%;background:#777}
.f-head{position:absolute;font-family:"Roboto",sans-serif;font-weight:700;font-size:18px;color:var(--white);letter-spacing:.3px}
.contact-item{position:absolute;left:358px;display:flex;gap:16px;font-weight:500;font-size:16px;line-height:21px;color:var(--white)}
.contact-item svg{flex:none;margin-top:2px}
.quick-links{position:absolute;left:602px;top:102px;list-style:none;font-size:15.5px;line-height:27.3px}
.news-text{position:absolute;left:782px;top:110px;width:270px;font-size:15.5px;line-height:21px}
.news-input{position:absolute;left:781px;top:168px;width:273px;height:37px;border-radius:19px;background:var(--white);color:#666;font-size:12.5px;padding:11px 0 0 16px}
.news-btn{position:absolute;left:782px;top:221px;width:138px;height:34px;border-radius:17px;background:var(--grey-btn);color:var(--white);font-family:"Roboto",sans-serif;font-weight:700;font-size:14px;display:flex;align-items:center;justify-content:center}
.footer-rule{position:absolute;left:0;top:355px;width:1200px;height:1px;background:#3a3a3a}
.copyright{position:absolute;left:0;top:402px;width:1200px;text-align:center;font-size:15.5px;color:var(--white)}
</style>
</head>
<body>

<header class="site-header">
  <nav class="main-nav">
    <a class="active" style="left:427px">HOME</a>
    <a style="left:516px">ABOUT US</a>
    <a style="left:634px">OUR PRODUCTS</a>
    <a style="left:788px">BLOG</a>
    <a style="left:872px">CONTACT US</a>
  </nav>
  <div class="lang">EN
    <svg width="9" height="6" viewBox="0 0 9 6"><path d="M1 1l3.5 3.5L8 1" fill="none" stroke="#333" stroke-width="1.4"/></svg>
  </div>
</header>
<div class="brand-tab"><span class="brand-mark"></span><span class="brand-name">Kelvaro</span></div>

<section class="hero" role="img" aria-label="Man in white thobe and red-and-white checked shemagh working at a laptop beside a green plant">
  <h1 class="hero-title">High Quality<br>Cotton Fabrics<br>Products</h1>
  <div class="btn-outline">LEARN MORE</div>
  <div class="dots"><span></span><span></span><span class="on"></span><span></span><span></span></div>
</section>

<section class="products">
  <div class="eyebrow center" style="top:58px">KELVARO GMBH</div>
  <h2 class="section-title center" style="top:88px">OUR PRODUCTS</h2>

  <svg class="carousel-arrow" style="left:57px" width="42" height="42" viewBox="0 0 42 42"><circle cx="21" cy="21" r="19" fill="#fff" stroke="#555" stroke-width="2.5"/><path d="M25 12l-11 9 11 9z" fill="#555"/></svg>
  <svg class="carousel-arrow" style="left:1102px" width="42" height="42" viewBox="0 0 42 42"><circle cx="21" cy="21" r="19" fill="#fff" stroke="#555" stroke-width="2.5"/><path d="M17 12l11 9-11 9z" fill="#555"/></svg>

  <article class="product-card" style="left:144px">
    <div class="product-img" role="img" aria-label="Folded white Swiss ghutra cloth" style="background:linear-gradient(135deg,#f2f2f2,#bdbdbd 55%,#2a2a2a)"></div>
    <h3>SWISS GHUTRA</h3>
    <p>Kelvaro has been a family-run textile business for 17 years with no web presence.</p>
  </article>
  <article class="product-card" style="left:458px">
    <div class="product-img" role="img" aria-label="Red and white checked shemagh fabric" style="background:linear-gradient(135deg,#d8485a,#f3e3e5 45%,#c9243a 75%,#efe9e9)"></div>
    <h3>SHEMAGH</h3>
    <p>Kelvaro has been a family-run textile business for 17 years with no web presence.</p>
  </article>
  <article class="product-card" style="left:770px">
    <div class="product-img" role="img" aria-label="Group of young men in white desdasha garments reading together" style="background:linear-gradient(135deg,#e8e4df,#f6f6f4 45%,#c9a79b 75%,#eceae7)"></div>
    <h3>DESDASHA’S</h3>
    <p>Kelvaro has been a family-run textile business for 17 years with no web presence.</p>
  </article>

  <div class="btn-outline" style="left:456px;top:610px;width:235px;height:53px">VIEW ALL</div>
</section>

<section class="welcome">
  <div class="welcome-img" role="img" aria-label="Man in white t-shirt wearing a red-and-white shemagh in an office"></div>
  <h2>Welcome to<br>Kelvaro</h2>
  <div class="rule"></div>
  <p>Kelvaro has been a family-run textile business for 17 years with no web presence. The majority of our historical sales have been based on pre-existing relationships or word-of-mouth connections. Now, we seek to diversify our customer base</p>
  <div class="btn-outline" style="left:746px;top:1981px;width:236px;height:52px">LEARN MORE</div>
</section>

<section class="process">
  <div class="eyebrow center" style="top:50px">Kelvaro GmbH</div>
  <h2 class="section-title center" style="top:85px">WHAT WE DO</h2>
  <div class="bar" style="left:566px;top:141px;width:68px"></div>

  <svg class="abs" style="left:0;top:0" width="1200" height="444" viewBox="0 0 1200 444" fill="none" stroke="#777" stroke-width="2.2" stroke-dasharray="4 4">
    <path d="M203 235c30-14 60-6 72 12 8 14-12 20-8 6 4-10 30-8 46-6"/>
    <path d="M441 235c30-16 60-8 72 10 8 14-12 20-8 6 4-10 30-8 46-6"/>
    <path d="M676 226c30-8 60 0 72 16 8 14-12 20-8 6 4-10 30-6 46-4"/>
    <path d="M905 235c30-16 60-8 72 10 8 14-12 20-8 6 4-10 30-8 46-6"/>
  </svg>
  <svg class="abs" style="left:0;top:0" width="1200" height="444" viewBox="0 0 1200 444" fill="#777">
    <path d="M322 250l-8-6v12z"/><path d="M560 248l-8-6v12z"/><path d="M795 246l-8-6v12z"/><path d="M1024 248l-8-6v12z"/>
  </svg>

  <div class="step" style="left:50px;top:173px">
    <div class="icon"><svg width="44" height="44" viewBox="0 0 44 44" fill="none" stroke="#333" stroke-width="2"><circle cx="28" cy="10" r="5"/><path d="M16 20l10 4 6 14M20 26l-6 14M10 30c6 0 10 6 10 10"/></svg></div>
    <h4>DESIGN<br>AND DEVELOP</h4>
  </div>
  <div class="step" style="left:288px;top:211px">
    <div class="icon"><svg width="44" height="44" viewBox="0 0 44 44" fill="none" stroke="#333" stroke-width="2"><path d="M12 8h22M22 8v16"/><ellipse cx="22" cy="32" rx="14" ry="6"/><ellipse cx="22" cy="32" rx="6" ry="2.5"/></svg></div>
    <h4>WEAVE</h4>
    <p>Special Weaving<br>Embroidery Technique</p>
  </div>
  <div class="step" style="left:524px;top:173px">
    <div class="icon"><svg width="44" height="44" viewBox="0 0 44 44" fill="none" stroke="#333" stroke-width="2"><circle cx="10" cy="16" r="5"/><circle cx="10" cy="28" r="5"/><path d="M14 19l24 8M14 25l24-8"/></svg></div>
    <h4>SHEAR</h4>
    <p>Neque porro<br>quisquam est qui</p>
  </div>
  <div class="step" style="left:756px;top:211px">
    <div class="icon"><svg width="44" height="44" viewBox="0 0 44 44" fill="none" stroke="#333" stroke-width="2"><path d="M34 6L8 38"/><circle cx="30" cy="12" r="6"/><path d="M14 10c10 6 18 16 20 26"/></svg></div>
    <h4>SEWING</h4>
    <p>Neque porro<br>quisquam est qui</p>
  </div>
  <div class="step" style="left:988px;top:173px">
    <div class="icon"><svg width="46" height="44" viewBox="0 0 46 44" fill="none" stroke="#333" stroke-width="2.2"><path d="M8 14l15-7 15 7-15 7zM8 14v16l15 8 15-8V14M23 21v17"/></svg></div>
    <h4>FINISH</h4>
    <p>Logo printing<br>Packing</p>
  </div>
</section>

<section class="enquiry">
  <h2 class="section-title center enquiry-title" style="font-size:33px">ENQUIRY FORM</h2>
  <div class="bar" style="left:566px;top:2729px;width:68px;height:3px;background:#999"></div>
  <div class="field" style="left:143px;top:2768px;width:297px;height:53px">Name</div>
  <div class="field" style="left:451px;top:2768px;width:295px;height:53px">email</div>
  <div class="field" style="left:759px;top:2768px;width:295px;height:53px">Phone</div>
  <div class="field msg" style="left:143px;top:2841px;width:913px;height:110px">Message</div>
  <div class="btn-dark">SUBMIT</div>
</section>

<footer class="site-footer">
  <div class="footer-brand"><span class="mark"></span>Kelvaro</div>
  <div class="social"><span></span><span></span><span></span><span></span></div>

  <div class="f-head" style="left:358px;top:60px">CONTACT US</div>
  <div class="contact-item" style="top:118px">
    <svg width="18" height="20" viewBox="0 0 18 20"><path d="M9 0a7 7 0 0 0-7 7c0 5 7 13 7 13s7-8 7-13a7 7 0 0 0-7-7zm0 10a3 3 0 1 1 0-6 3 3 0 0 1 0 6z" fill="#fff"/></svg>
    <span>Kelvaro GmbH<br>8455 enim ipsam<br>voluptatem quia</span>
  </div>
  <div class="contact-item" style="top:188px">
    <svg width="18" height="18" viewBox="0 0 18 18"><path d="M4 1l3 4-2 2c1 3 3 5 6 6l2-2 4 3-2 3C8 17 1 10 1 3z" fill="#fff"/></svg>
    <span>888 4417 2960</span>
  </div>
  <div class="contact-item" style="top:223px">
    <svg width="18" height="16" viewBox="0 0 18 16"><rect x="0" y="2" width="18" height="13" rx="1.5" fill="#fff"/><path d="M1 3l8 6 8-6" fill="none" stroke="#242424" stroke-width="1.6"/></svg>
    <span>info@kelvaro.com</span>
  </div>
  <div class="contact-item" style="top:261px">
    <svg width="18" height="18" viewBox="0 0 18 18"><circle cx="9" cy="9" r="9" fill="#fff"/><path d="M9 4v5l3 2" fill="none" stroke="#242424" stroke-width="1.8"/></svg>
    <span>Monday to Friday<br>9am to 5pm</span>
  </div>

  <div class="f-head" style="left:598px;top:59px">QUICK LINKS</div>
  <ul class="quick-links">
    <li>Home</li><li>About Us</li><li>Our Products</li><li>Contact Us</li><li>Blog</li><li>How It Works</li>
  </ul>

  <div class="f-head" style="left:782px;top:59px">SIGN UP FOR NEWSLETTER</div>
  <p class="news-text">Sed ut perspiciatis unde omnis iste natus error sit voluptatem</p>
  <div class="news-input">Enter email</div>
  <div class="news-btn">SUBSCRIBE</div>

  <div class="footer-rule"></div>
  <p class="copyright">Kelvaro GmbH © 2021 All Rights Reserved | Privacy Policy | Terms and Conditions</p>
</footer>

</body>
</html>
```